Retail Jewelry Business Card Design Project

We are in need of a new business card design for a retail jewelry store. This store is in the business of fine jewelry including but not specific to bridal jewelry, diamonds, designer jewelry and watches.

This store has been in business for 20 years but continues to strive for a modern professional appeal. The main colors use for this business are a royal blue, white and silver.

Target Market(s)

Target market is ages 18-50

Industry/Entity Type

Jewelry

Requirements
Must have
• Sales Person Name
Sales Person Email Address

Store Address
Store Phone
Website

Standard business card size. No odd shapes or sizes.
Nice to have
• Overall modern feel for card.

We have thought that a design with a nice feature of the logo on the back of the card would be nice but open to ideas.
Should not have
• No specific images of jewelry should be used.

```html
<!DOCTYPE html>
<html lang="en">
<head>
<meta charset="utf-8">
<title>Marlow Reed Fine Jewelry – Business Card</title>
<link href="https://fonts.googleapis.com/css2?family=Open+Sans:wght@400;600;700&display=swap" rel="stylesheet">
<style>
  :root {
    --royal: #2e3191;
    --lavender: #7b72b8;
    --ink: #333333;
    --paper: #ffffff;
    --canvas: #ffffff;
    --shadow: rgba(0, 0, 0, 0.35);
  }
  * { margin: 0; padding: 0; box-sizing: border-box; }
  html, body {
    width: 1200px;
    height: 1000px;
    overflow: hidden;
    background: var(--canvas);
    font-family: "Open Sans", Arial, sans-serif;
  }
  .stage { position: relative; width: 1200px; height: 1000px; }

  .card {
    position: absolute;
    left: 281px;
    width: 660px;
    height: 376px;
    box-shadow: 4px 5px 7px var(--shadow);
    overflow: hidden;
  }

  /* Front */
  .card--front { top: 98px; background: var(--royal); color: var(--paper); }
  .card--front .wordmark {
    position: absolute;
    top: 150px;
    left: 0;
    width: 100%;
    text-align: center;
    font-weight: 600;
    font-size: 38px;
    line-height: 1.2;
    color: var(--paper);
  }
  .card--front .website {
    position: absolute;
    top: 320px;
    left: 0;
    width: 100%;
    text-align: center;
    font-size: 16px;
    letter-spacing: 1.3px;
  }

  /* Back */
  .card--back { top: 533px; background: var(--paper); }
  .card--back .wordmark {
    position: absolute;
    top: 70px;
    right: 48px;
    width: 330px;
    text-align: center;
    font-weight: 600;
    font-size: 34px;
    line-height: 1.2;
    color: var(--royal);
  }
  .tab {
    position: absolute;
    left: 0;
    top: 271px;
    width: 15px;
    height: 66px;
    background: var(--lavender);
    border-radius: 0 10px 10px 0;
  }
  .person { position: absolute; left: 50px; top: 280px; }
  .person__name { font-size: 19px; font-weight: 700; color: var(--royal); }
  .person__name .surname { color: var(--lavender); }
  .person__role { font-size: 15px; color: var(--ink); margin-top: 2px; }

  .address {
    position: absolute;
    right: 13px;
    top: 204px;
    text-align: right;
    font-size: 16px;
    line-height: 22px;
    color: var(--ink);
    font-style: normal;
  }
  .contacts {
    position: absolute;
    right: 41px;
    top: 262px;
    list-style: none;
    font-size: 16px;
    line-height: 22.5px;
    color: var(--ink);
    text-align: right;
  }
  .contacts li { position: relative; }
  .contacts .icon {
    position: absolute;
    right: -28px;
    top: 4px;
    width: 16px;
    height: 15px;
  }
</style>
</head>
<body>
<main class="stage">

  <section class="card card--front" aria-label="Card front">
    <div class="wordmark">Marlow Reed<br>Fine Jewelry</div>
    <div class="website">www.marlowreedjewelry.com</div>
  </section>

  <section class="card card--back" aria-label="Card back">
    <div class="wordmark">Marlow Reed<br>Fine Jewelry</div>

    <address class="address">2280 Linden Avenue<br>Bay Harbor, FL 32409</address>

    <ul class="contacts">
      <li>000.000.0000
        <svg class="icon" viewBox="0 0 16 15" aria-hidden="true">
          <path d="M1 5 Q8 0 15 5 L13 7 L11 5.5 L5 5.5 L3 7 Z" fill="#7b72b8"/>
          <path d="M4 7 L12 7 L14 13 L2 13 Z" fill="#7b72b8"/>
          <circle cx="8" cy="10" r="1.6" fill="#fff"/>
        </svg>
      </li>
      <li>evan@marlowreedjewelry.com
        <svg class="icon" viewBox="0 0 16 15" aria-hidden="true">
          <rect x="0.5" y="2" width="15" height="11" fill="#7b72b8"/>
          <path d="M0.5 2 L8 8.5 L15.5 2 M0.5 13 L6 7.5 M15.5 13 L10 7.5" stroke="#fff" stroke-width="1.2" fill="none"/>
        </svg>
      </li>
      <li>www.marlowreedjewelry.com
        <svg class="icon" viewBox="0 0 16 15" aria-hidden="true">
          <circle cx="8" cy="7.5" r="6.8" fill="none" stroke="#7b72b8" stroke-width="1.3"/>
          <ellipse cx="8" cy="7.5" rx="3" ry="6.8" fill="none" stroke="#7b72b8" stroke-width="1.1"/>
          <path d="M1.2 7.5 H14.8 M2.5 4 H13.5 M2.5 11 H13.5" stroke="#7b72b8" stroke-width="1.1"/>
        </svg>
      </li>
    </ul>

    <div class="tab"></div>
    <div class="person">
      <div class="person__name">Evan Marlow <span class="surname">Castell</span></div>
      <div class="person__role">Owner</div>
    </div>
  </section>

</main>
</body>
</html>
```